Social Media Banner with Company Logo

We need company banner for social media sites: Linkedin, Twitter, and Facebook. We are looking for quality (royalty free) images of locations our customers can identify with and our company logo incorporated into those locations in a very natural way. Our customers are business owners and financial advisors. We will eventually want 12 different design concepts that all play off of the same theme of locations and our logo.

```html
<!DOCTYPE html>
<html lang="en">
<head>
<meta charset="utf-8">
<title>Summit Pension Partners – Social Banner</title>
<link rel="stylesheet" href="https://fonts.googleapis.com/css2?family=Roboto:wght@400;500;700&family=Kalam:wght@400&display=swap">
<style>
  :root {
    --page-bg: #e6e9ec;
    --banner-white: #ffffff;
    --panel-grey: #eeedee;
    --accent-green: #8cc63f;
    --brand-blue: #1f78b4;
    --text-grey: #4a4a4a;
    --photo-backdrop: #e8e9e7;
    --photo-warm: #dcbfa8;
    --photo-hair: #b08a6c;
    --photo-cool: #d9e1e6;
  }
  * { box-sizing: border-box; margin: 0; padding: 0; }
  html, body {
    width: 1200px;
    height: 1200px;
    overflow: hidden;
    background: var(--page-bg);
  }
  .canvas {
    position: relative;
    width: 1200px;
    height: 1200px;
  }
  .banner {
    position: absolute;
    left: 26px;
    top: 388px;
    width: 1147px;
    height: 425px;
    background: var(--banner-white);
    overflow: hidden;
    font-family: "Roboto", Arial, sans-serif;
  }
  .banner-shapes {
    position: absolute;
    inset: 0;
    width: 1147px;
    height: 425px;
  }
  .headline {
    position: absolute;
    left: 58px;
    top: 106px;
    font-weight: 500;
    font-size: 44px;
    line-height: 59px;
    color: var(--brand-blue);
    text-transform: uppercase;
  }
  .tagline {
    position: absolute;
    left: 58px;
    top: 286px;
    font-family: "Kalam", "Comic Sans MS", cursive;
    font-size: 17px;
    color: var(--brand-blue);
  }
  .brand {
    position: absolute;
    left: 908px;
    top: 24px;
    display: flex;
    align-items: center;
    gap: 12px;
  }
  .brand-mark {
    width: 40px;
    height: 40px;
    background: var(--accent-green);
  }
  .brand-name {
    font-weight: 500;
    font-size: 14px;
    line-height: 17px;
    color: var(--brand-blue);
    text-transform: uppercase;
    letter-spacing: 0.6px;
  }
  .join-button {
    position: absolute;
    left: 937px;
    top: 326px;
    width: 173px;
    height: 42px;
    border-radius: 4px;
    background: var(--brand-blue);
    color: #fff;
    display: flex;
    align-items: center;
    justify-content: center;
    gap: 10px;
    font-weight: 700;
    font-size: 17px;
    letter-spacing: 1.6px;
    text-transform: uppercase;
  }
  .join-button svg { width: 12px; height: 14px; }
  .site-url {
    position: absolute;
    left: 917px;
    top: 376px;
    width: 213px;
    text-align: center;
    font-size: 14px;
    letter-spacing: 0.5px;
    color: var(--text-grey);
  }
</style>
</head>
<body>
<div class="canvas">
  <section class="banner">
    <svg class="banner-shapes" viewBox="0 0 956 354" preserveAspectRatio="none">
      <defs>
        <linearGradient id="portrait-tones" x1="0" y1="0" x2="1" y2="0.3">
          <stop offset="0" stop-color="var(--photo-backdrop)"/>
          <stop offset="0.3" stop-color="var(--photo-warm)"/>
          <stop offset="0.6" stop-color="var(--photo-hair)" stop-opacity="0.75"/>
          <stop offset="1" stop-color="var(--photo-cool)"/>
        </linearGradient>
      </defs>
      <path class="accent-corner" d="M0,150 C15,240 40,300 75,354 H0 Z" fill="var(--accent-green)"/>
      <path class="grey-panel" d="M0,0 H400 L410,354 H75 C40,300 15,240 0,150 Z" fill="var(--panel-grey)"/>
      <circle class="accent-arc" cx="521" cy="158" r="228" fill="var(--accent-green)"/>
      <circle class="portrait" cx="537" cy="172" r="228" fill="url(#portrait-tones)" role="img" aria-label="Portrait photo of a smiling young man wearing glasses"/>
    </svg>

    <h1 class="headline">Summit<br>Pension<br>Partners</h1>
    <p class="tagline">Plan For The Future. Follow The Leader</p>

    <div class="brand">
      <span class="brand-mark"></span>
      <span class="brand-name">Summit<br>Pension<br>Partners</span>
    </div>

    <div class="join-button">Join Now
      <svg viewBox="0 0 12 14"><path d="M1,1 L11,7 L1,13 L4,7 Z" fill="#fff"/></svg>
    </div>
    <p class="site-url">summitpension.com</p>
  </section>
</div>
</body>
</html>
```